BrivoMatex. Lantern for the Steady Growth. Business card

Professional business card for BrivoMatex (Lantern for the Steady Growth)
My rationale: Strategy-> Execution-> Results-> Value that lead to the BrivoMatex name: We put the Lantern for the Steady Growth.
We deliver value to our customers helping them at defining a good strategy (cyan arrow). 90% of well formulated strategies fail due to poor execution so we also consider strategical execution very important (green arrow). Due to the execution we obtain the results (blue arrow). Finally, the results provide feedback to redefine strategy, and the new strategy has to be executed and new results obtained providing new feedback and on and on. It's like a wheel that finally, must create corporate value: value for shareholders, staholders, employees, providers...-

Target Market(s)

CEOs and steering comitees , invewrnent funds

Industry/Entity Type

Business Consultant

Contact Information for Business Card

Tommaso Ferlini
CEO & Founder
tommaso.ferlini@brivomatex.example
Mobile: +34 611.205.938
www.brivomatex.example

Colors

Designer to choose colors to be used in the design.

Requirements
Nice to have
• Nice to hace the words: Strategy, execution, results
• Nice to vave the claim: Lantern for the Steady Growth
• The three colors should be shown:
• cyan for STRATEGY
• green for EXECUTION
• blue for RESULTS
Should not have
• Complete black background

```html
<!DOCTYPE html>
<html lang="en">
<head>
<meta charset="utf-8">
<title>BrivoMatex — Business Card</title>
<link href="https://fonts.googleapis.com/css2?family=Roboto:wght@400;700&display=swap" rel="stylesheet">
<style>
  :root {
    --blue: #0b3a9a;
    --green: #8dc63f;
    --cyan: #1aaee8;
    --grey: #555a60;
    --paper: #ffffff;
    --backdrop: #d9d9d9;
  }
  * { box-sizing: border-box; margin: 0; padding: 0; }
  html, body {
    width: 1200px; height: 800px; overflow: hidden;
    background: var(--backdrop);
    font-family: "Roboto", Arial, sans-serif;
  }
  .stage {
    width: 1200px; height: 800px;
    display: flex; align-items: center; justify-content: center; gap: 40px;
  }
  .card {
    position: relative;
    width: 540px; height: 309px;
    background: var(--paper);
    box-shadow: 0 6px 18px rgba(0,0,0,.18);
  }
  /* Front side */
  .brand-name {
    font-weight: 700; color: var(--blue); letter-spacing: -0.5px;
    display: flex; align-items: center; gap: 8px;
  }
  .brand-dot { width: 12px; height: 12px; border-radius: 50%; background: var(--blue); }
  .card-front .brand-name {
    position: absolute; right: 44px; top: 66px; font-size: 30px;
  }
  .divider {
    position: absolute; left: 34px; right: 34px; top: 172px; height: 2px;
    display: flex;
  }
  .divider span { flex: 1; }
  .divider .seg-blue { background: var(--blue); }
  .divider .seg-green { background: var(--green); }
  .divider .seg-cyan { background: var(--cyan); }
  .person {
    position: absolute; left: 34px; top: 124px;
  }
  .person-name { font-weight: 700; font-size: 19px; color: var(--blue); }
  .person-title { font-size: 13px; color: var(--green); margin-top: 2px; }
  .contacts {
    position: absolute; left: 34px; top: 188px; list-style: none;
    font-size: 12px; color: var(--grey); line-height: 19px;
  }
  .contacts li { display: flex; align-items: center; gap: 8px; }
  .contacts svg { width: 12px; height: 12px; flex: none; }
  /* Back side */
  .card-back .brand-name {
    position: absolute; right: 40px; top: 168px; font-size: 52px;
  }
  .card-back .brand-name .brand-dot { width: 20px; height: 20px; }
  .card-back .web {
    position: absolute; right: 42px; top: 232px;
    font-size: 13px; letter-spacing: 5px; color: var(--grey);
  }
</style>
</head>
<body>
<main class="stage">
  <section class="card card-front" aria-label="Business card front">
    <div class="brand-name">BrivoMatex</div>
    <div class="person">
      <div class="person-name">Tommaso Ferlini</div>
      <div class="person-title">CEO &amp; Founder</div>
    </div>
    <div class="divider"><span class="seg-blue"></span><span class="seg-green"></span><span class="seg-cyan"></span></div>
    <ul class="contacts">
      <li>
        <svg viewBox="0 0 12 12"><rect x="3" y="0.5" width="6" height="11" rx="1" fill="none" stroke="var(--blue)" stroke-width="1.2"/><circle cx="6" cy="9.5" r=".7" fill="var(--blue)"/></svg>
        +34 611.205.938
      </li>
      <li>
        <svg viewBox="0 0 12 12"><rect x=".5" y="2" width="11" height="8" fill="var(--blue)"/><path d="M.5 2 6 6.5 11.5 2" fill="none" stroke="#fff" stroke-width="1"/></svg>
        tommaso.ferlini@brivomatex.example
      </li>
      <li>
        <svg viewBox="0 0 12 12"><circle cx="6" cy="6" r="5.4" fill="none" stroke="var(--blue)" stroke-width="1.2"/><ellipse cx="6" cy="6" rx="2.2" ry="5.4" fill="none" stroke="var(--blue)" stroke-width="1"/><path d="M.6 6h10.8" stroke="var(--blue)" stroke-width="1"/></svg>
        www.brivomatex.example
      </li>
    </ul>
  </section>

  <section class="card card-back" aria-label="Business card back">
    <div class="brand-name"><span class="brand-dot"></span>BrivoMatex</div>
    <div class="web">www.brivomatex.example</div>
  </section>
</main>
</body>
</html>
```